Velka Haven

Yoga and Pilates
I teach privates and small groups

Simple clean design 2-4 pages.
(Bookings will be though contacting me, so need for booking capabilities)

```html
<!DOCTYPE html>
<html lang="en">
<head>
<meta charset="utf-8">
<title>Velka Haven — Yoga and Pilates</title>
<link href="https://fonts.googleapis.com/css2?family=Roboto:wght@400;500;700;900&display=swap" rel="stylesheet">
<style>
  :root{
    --ink:#111111;
    --text:#5e5e5e;
    --white:#ffffff;
    --mist:#c2d6dd;
    --btn:#c2d6dd;
    --btn-ink:#1f2b30;
    --frame:#e6e6e6;
    --line:#d8d8d8;
  }
  *{margin:0;padding:0;box-sizing:border-box;}
  html,body{width:1200px;height:3984px;overflow:hidden;}
  body{position:relative;background:var(--white);font-family:"Roboto",sans-serif;color:var(--ink);}
  .abs{position:absolute;}
  a{color:inherit;text-decoration:none;}

  /* buttons */
  .btn{position:absolute;display:flex;align-items:center;justify-content:center;gap:10px;
       font-size:14px;font-weight:700;text-transform:uppercase;color:var(--btn-ink);background:var(--btn);border-radius:3px;letter-spacing:.1px;}
  .btn svg{width:14px;height:14px;}
  .btn--white{background:var(--white);}
  .btn--dark{background:var(--ink);color:var(--white);}

  /* hero */
  .hero{position:absolute;left:0;top:0;width:1200px;height:625px;
        background:
          radial-gradient(ellipse 220px 330px at 880px 330px, rgba(210,170,120,.55), transparent 70%),
          radial-gradient(ellipse 700px 160px at 300px 570px, rgba(90,100,70,.9), transparent 70%),
          linear-gradient(180deg,#1f4a30 0%,#2b5b3c 35%,#20403a 60%,#283a2e 100%);}
  .hero__shade{position:absolute;inset:0;background:linear-gradient(90deg,rgba(0,0,0,.35),rgba(0,0,0,0) 60%);}
  .brand{position:absolute;font-weight:700;font-size:24px;letter-spacing:-.5px;text-transform:uppercase;}
  .nav{position:absolute;top:44px;display:flex;font-size:15px;font-weight:500;}
  .nav--top{left:432px;gap:0;color:var(--white);}
  .nav--top a{margin-right:34px;}
  .hero__title{position:absolute;left:111px;top:258px;font-size:45px;font-weight:700;color:var(--white);letter-spacing:-1px;}
  .hero__lead{position:absolute;left:111px;top:330px;width:480px;font-size:17px;line-height:27px;font-weight:500;color:var(--white);}

  /* section titles */
  .section-title{position:absolute;left:0;width:1200px;text-align:center;font-size:44px;font-weight:900;letter-spacing:-1.5px;text-transform:uppercase;}

  /* service rows */
  .photo{position:absolute;width:440px;height:367px;background:var(--white);border:1px solid var(--frame);box-shadow:0 0 6px rgba(0,0,0,.12);padding:6px;}
  .photo div{width:100%;height:100%;}
  .row-title{position:absolute;font-size:31px;font-weight:500;letter-spacing:-.5px;}
  .row-text{position:absolute;width:450px;font-size:14.5px;line-height:25.7px;color:var(--text);text-align:justify;}

  .why{position:absolute;left:0;top:2489px;width:1200px;height:421px;background:var(--mist);}
  .why__text{position:absolute;left:110px;top:163px;width:980px;text-align:center;font-size:14.5px;line-height:27px;color:var(--text);}

  .news{position:absolute;left:0;top:3462px;width:1200px;height:310px;background:var(--mist);}
  .field{position:absolute;top:134px;width:318px;height:48px;background:var(--white);display:flex;align-items:center;justify-content:space-between;padding:0 18px;font-size:13px;color:#9a9a9a;}
  .field svg{width:12px;height:12px;}

  .foot-links{position:absolute;top:3847px;left:650px;display:flex;font-size:14px;font-weight:500;}
  .foot-links a{margin-left:31px;}
  .copy{position:absolute;left:110px;top:3903px;font-size:13px;color:#333;}
  .social{position:absolute;top:3892px;width:31px;height:31px;border-radius:50%;border:1px solid var(--line);background:var(--white);}
</style>
</head>
<body>

<header class="hero" role="img" aria-label="Photo of a woman meditating cross-legged on a rock by a forest stream">
  <div class="hero__shade"></div>
</header>
<div class="brand" style="left:111px;top:40px;color:var(--white);">Velka Haven</div>
<nav class="nav nav--top">
  <a>Home</a><a>About</a><a>Our Services</a><a>Reviews</a><a>Blog</a><a>Contact</a>
</nav>
<a class="btn" style="left:960px;top:32px;width:128px;height:44px;font-size:13px;">Book now
  <svg viewBox="0 0 14 14"><circle cx="7" cy="7" r="7" fill="currentColor"/><path d="M5.5 4l3 3-3 3" stroke="#c2d6dd" stroke-width="1.8" fill="none"/></svg></a>
<h1 class="hero__title">VELKA HAVEN</h1>
<p class="hero__lead">Lorem ipsum dolor sit amet, consectetur adipiscing elit, sed do eiusmod tempor incididunt ut labore</p>
<a class="btn" style="left:111px;top:413px;width:172px;height:48px;">Get started
  <svg viewBox="0 0 14 14"><circle cx="7" cy="7" r="7" fill="currentColor"/><path d="M5.5 4l3 3-3 3" stroke="#c2d6dd" stroke-width="1.8" fill="none"/></svg></a>

<h2 class="section-title" style="top:690px;">Our Service</h2>

<!-- row 1 -->
<div class="photo" style="left:110px;top:788px;"><div role="img" aria-label="Photo of a woman in a seated yoga pose before misty mountains at sunset" style="background:linear-gradient(180deg,#e7c3a0 0%,#c9a07e 45%,#7d6250 75%,#4b3b34 100%);"></div></div>
<h3 class="row-title" style="left:634px;top:828px;">Lorem Ipsum Dolor</h3>
<p class="row-text" style="left:637px;top:884px;">Sed ut perspiciatis unde omnis iste natus error sit voluptatem accusantium doloremque laudantium, totam rem aperiam, eaque ipsa quae ab illo inventore veritatis et quasi architecto beatae vitae dicta sunt explicabo. Nemo enim ipsam voluptatem quia voluptas sit aspernatur aut odit aut fugit, sed quia consequuntur magni dolores eos qui ratione voluptatem sequi nesciunt.</p>
<a class="btn" style="left:637px;top:1062px;width:145px;height:44px;">Learn more
  <svg viewBox="0 0 14 14"><circle cx="7" cy="7" r="7" fill="currentColor"/><path d="M5.5 4l3 3-3 3" stroke="#c2d6dd" stroke-width="1.8" fill="none"/></svg></a>

<!-- row 2 -->
<h3 class="row-title" style="left:110px;top:1240px;">Lorem Ipsum Dolor</h3>
<p class="row-text" style="left:112px;top:1296px;">Sed ut perspiciatis unde omnis iste natus error sit voluptatem accusantium doloremque laudantium, totam rem aperiam, eaque ipsa quae ab illo inventore veritatis et quasi architecto beatae vitae dicta sunt explicabo. Nemo enim ipsam voluptatem quia voluptas sit aspernatur aut odit aut fugit, sed quia consequuntur magni dolores eos qui ratione voluptatem sequi nesciunt.</p>
<a class="btn" style="left:112px;top:1473px;width:147px;height:44px;">Learn more
  <svg viewBox="0 0 14 14"><circle cx="7" cy="7" r="7" fill="currentColor"/><path d="M5.5 4l3 3-3 3" stroke="#c2d6dd" stroke-width="1.8" fill="none"/></svg></a>
<div class="photo" style="left:648px;top:1200px;"><div role="img" aria-label="Photo of a woman doing a pilates exercise on a mat with a ring" style="background:linear-gradient(135deg,#e9e4dc 0%,#d8d0c6 40%,#9a958f 65%,#3a3b3d 100%);"></div></div>

<!-- row 3 -->
<div class="photo" style="left:110px;top:1611px;"><div role="img" aria-label="Photo of a group class resting in child's pose on yoga mats" style="background:linear-gradient(180deg,#c7a27d 0%,#9d8f88 35%,#d58b74 55%,#7fb1c2 72%,#b27c4f 100%);"></div></div>
<h3 class="row-title" style="left:634px;top:1651px;">Lorem Ipsum Dolor</h3>
<p class="row-text" style="left:637px;top:1707px;">Sed ut perspiciatis unde omnis iste natus error sit voluptatem accusantium doloremque laudantium, totam rem aperiam, eaque ipsa quae ab illo inventore veritatis et quasi architecto beatae vitae dicta sunt explicabo. Nemo enim ipsam voluptatem quia voluptas sit aspernatur aut odit aut fugit, sed quia consequuntur magni dolores eos qui ratione voluptatem sequi nesciunt.</p>
<a class="btn" style="left:637px;top:1885px;width:145px;height:44px;">Learn more
  <svg viewBox="0 0 14 14"><circle cx="7" cy="7" r="7" fill="currentColor"/><path d="M5.5 4l3 3-3 3" stroke="#c2d6dd" stroke-width="1.8" fill="none"/></svg></a>

<!-- row 4 -->
<h3 class="row-title" style="left:110px;top:2063px;">Lorem Ipsum Dolor</h3>
<p class="row-text" style="left:112px;top:2119px;">Sed ut perspiciatis unde omnis iste natus error sit voluptatem accusantium doloremque laudantium, totam rem aperiam, eaque ipsa quae ab illo inventore veritatis et quasi architecto beatae vitae dicta sunt explicabo. Nemo enim ipsam voluptatem quia voluptas sit aspernatur aut odit aut fugit, sed quia consequuntur magni dolores eos qui ratione voluptatem sequi nesciunt.</p>
<a class="btn" style="left:112px;top:2296px;width:147px;height:44px;">Learn more
  <svg viewBox="0 0 14 14"><circle cx="7" cy="7" r="7" fill="currentColor"/><path d="M5.5 4l3 3-3 3" stroke="#c2d6dd" stroke-width="1.8" fill="none"/></svg></a>
<div class="photo" style="left:648px;top:2023px;"><div role="img" aria-label="Photo of two women exercising on pilates reformer machines" style="background:linear-gradient(135deg,#8c4a24 0%,#b46a35 40%,#3b2f2a 60%,#a0582c 100%);"></div></div>

<!-- why choose us -->
<section class="why">
  <h2 class="section-title" style="top:88px;">Why Choose Us</h2>
  <p class="why__text">Lorem ipsum dolor sit amet, consectetur adipiscing elit, sed do eiusmod tempor incididunt ut labore et dolore magna aliqua. Ut enim ad minim veniam, quis nostrud exercitation ullamco laboris nisi ut aliquip ex ea commodo consequat. Duis aute irure dolor in reprehenderit in voluptate velit esse cillum dolore eu fugiat nulla pariatur. Excepteur sint occaecat cupidatat non proident,</p>
  <a class="btn btn--white" style="left:505px;top:278px;width:189px;height:44px;">View all videos
    <svg viewBox="0 0 14 14"><circle cx="7" cy="7" r="7" fill="currentColor"/><path d="M5.5 4l3 3-3 3" stroke="#ffffff" stroke-width="1.8" fill="none"/></svg></a>
</section>

<!-- about -->
<div class="photo" style="left:110px;top:2996px;"><div role="img" aria-label="Photo of a woman in triangle pose on a mat on a green mountainside" style="background:linear-gradient(180deg,#5f86a8 0%,#6f8f86 45%,#5d7a4e 75%,#6e8f46 100%);"></div></div>
<h2 class="abs" style="left:637px;top:3030px;font-size:44px;font-weight:900;letter-spacing:-1.5px;">ABOUT US</h2>
<p class="row-text" style="left:637px;top:3097px;">Sed ut perspiciatis unde omnis iste natus error sit voluptatem accusantium doloremque laudantium, totam rem aperiam, eaque ipsa quae ab illo inventore veritatis et quasi architecto beatae vitae dicta sunt explicabo. Nemo enim ipsam voluptatem quia voluptas sit aspernatur aut odit aut fugit, sed quia consequuntur magni dolores eos qui ratione voluptatem sequi nesciunt.</p>
<a class="btn" style="left:637px;top:3275px;width:146px;height:44px;">Learn more
  <svg viewBox="0 0 14 14"><circle cx="7" cy="7" r="7" fill="currentColor"/><path d="M5.5 4l3 3-3 3" stroke="#c2d6dd" stroke-width="1.8" fill="none"/></svg></a>

<!-- newsletter -->
<section class="news">
  <h2 class="section-title" style="top:46px;font-size:38px;letter-spacing:-1.2px;">Newsletter Subscription</h2>
  <div class="field" style="left:110px;">First Name
    <svg viewBox="0 0 12 12"><circle cx="6" cy="3.5" r="2.7" fill="#333"/><path d="M1 12c0-4 2-5.5 5-5.5s5 1.5 5 5.5z" fill="#333"/></svg></div>
  <div class="field" style="left:439px;">Last Name
    <svg viewBox="0 0 12 12"><circle cx="6" cy="3.5" r="2.7" fill="#333"/><path d="M1 12c0-4 2-5.5 5-5.5s5 1.5 5 5.5z" fill="#333"/></svg></div>
  <div class="field" style="left:770px;">Email Address
    <svg viewBox="0 0 12 12"><rect x="0" y="2" width="12" height="8.5" rx="1" fill="#333"/><path d="M0.5 3l5.5 4 5.5-4" stroke="#fff" stroke-width="1.1" fill="none"/></svg></div>
  <a class="btn btn--dark" style="left:505px;top:204px;width:189px;height:46px;">Subscribe now</a>
</section>

<!-- footer -->
<footer>
  <div class="brand" style="left:110px;top:3832px;color:var(--ink);">Velka Haven</div>
  <nav class="foot-links"><a>Home</a><a>About</a><a>Our Services</a><a>Reviews</a><a>Blog</a><a>Contact</a></nav>
  <p class="copy">© 2022 Velka Haven. All Rights Reserved</p>
  <span class="social" style="left:916px;"></span>
  <span class="social" style="left:961px;"></span>
  <span class="social" style="left:1007px;"></span>
  <span class="social" style="left:1053px;"></span>
</footer>

</body>
</html>
```